Website for keystone mobile detailing.

Need a homepage, pages for: car and truck detailing, boat detailing, airplane detailing, about us, contact us. I have the domain name through nimbuspark so I will need the design uploaded on my domain. Also hoping to link other domains to this page.I would like to see the logo more pronounced. I would like to see a large phone number link to call my business. The layout looks nice but the pics need to depict car washing and waxing not car mechanics. i would like the colors of the webpage to incorporate the colors found in the logo in some way. I would like links to social media pages

Target Market(s)

Local customers in Vero Beach, Florida.

Number of Pages Required

5+ page

Colors

Designer to choose colors to be used in the design.

Requirements
Must have
• Easy to navigate, attractive pages with pictures and logo, professional looking. must have my phone number and logo very prevalent and links to call or go to home page. I would like links to my social media accounts on the home page.
Nice to have
• Easy to navigate, attractive pages with pictures and logo, professional looking.

```html
<!DOCTYPE html>
<html lang="en">
<head>
<meta charset="utf-8">
<title>Keystone Mobile Detailing</title>
<link href="https://fonts.googleapis.com/css2?family=Montserrat:wght@400;600;700&family=Open+Sans:wght@400;600;700&display=swap" rel="stylesheet">
<style>
:root{
  --blue:#1b96e6;
  --navy:#1f1769;
  --red:#e8131a;
  --white:#ffffff;
  --grey-bg:#efefef;
  --ink:#1e1e1e;
  --text:#3a3a3a;
  --rule:#e4e4e4;
}
*{margin:0;padding:0;box-sizing:border-box}
html,body{width:1200px;height:2769px;overflow:hidden}
body{position:relative;background:var(--white);font-family:"Open Sans",Arial,sans-serif;color:var(--text)}
.abs{position:absolute}
.heading{font-family:"Montserrat",Arial,sans-serif;font-weight:700}

/* header */
.site-header{left:0;top:0;width:1200px;height:115px;background:var(--white)}
.brand{left:132px;top:26px;display:flex;align-items:center;gap:12px;text-decoration:none}
.brand-dot{width:42px;height:42px;border-radius:50%;background:var(--navy)}
.brand-name{font-family:"Montserrat",Arial,sans-serif;font-weight:700;font-size:26px;line-height:1.05;color:var(--navy);width:240px}
.call-icon{left:785px;top:20px;width:40px;height:40px;border:2px solid var(--navy);border-radius:50%;display:flex;align-items:center;justify-content:center}
.call-label{left:838px;top:18px;font-family:"Montserrat",Arial,sans-serif;font-weight:700;font-size:10px;color:var(--ink);letter-spacing:.3px}
.call-number{left:836px;top:28px;font-family:"Montserrat",Arial,sans-serif;font-weight:700;font-size:34px;color:var(--red);text-decoration:none;letter-spacing:.5px}
.main-nav{left:487px;top:79px;display:flex}
.main-nav a{font-family:"Montserrat",Arial,sans-serif;font-weight:600;font-size:11px;color:var(--ink);text-decoration:none;padding:6px 9px;margin-right:19px}
.main-nav a.active{background:var(--red);color:var(--white)}

/* hero */
.hero{left:0;top:115px;width:1200px;height:533px;
  background:
    radial-gradient(ellipse 230px 200px at 600px 250px,rgba(250,250,252,.95) 0%,rgba(230,232,236,.7) 45%,rgba(230,232,236,0) 100%),
    radial-gradient(ellipse 90px 40px at 420px 240px,rgba(200,40,50,.55),rgba(200,40,50,0)),
    radial-gradient(ellipse 90px 40px at 790px 240px,rgba(200,40,50,.55),rgba(200,40,50,0)),
    linear-gradient(90deg,#3c4247 0%,#7a8088 18%,#9aa1a8 32%,#bfc4c9 50%,#9aa1a8 68%,#6f757c 84%,#3a3f44 100%),
    linear-gradient(180deg,#2a2e33 0%,#555a60 60%,#6a6055 100%);
  background-blend-mode:normal,normal,normal,multiply,normal}
.hero-caption{left:105px;top:267px;width:317px;height:200px;background:rgba(20,20,25,.62);padding:28px 10px 0 38px}
.hero-title{font-size:36px;line-height:42px;color:var(--white);white-space:nowrap}
.btn-blue{display:inline-block;margin-top:18px;background:var(--blue);color:var(--white);font-family:"Montserrat",Arial,sans-serif;font-weight:700;font-size:15px;padding:8px 18px;text-decoration:none}
.hero-dots{left:550px;top:473px;display:flex;gap:16px}
.hero-dots span{width:9px;height:9px;border-radius:50%;background:var(--white)}
.hero-dots span.on{background:var(--red);box-shadow:0 0 0 3px var(--white)}

/* services */
.services{left:0;top:648px;width:1200px;height:482px;background:var(--blue)}
.section-title{width:1200px;text-align:center;font-size:24px;color:var(--white)}
.title-rule{width:50px;height:3px;background:var(--white);left:575px}
.service-card{top:129px;width:301px;height:306px;overflow:hidden}
.service-photo{width:100%;height:100%}
.photo-wash{background:
  radial-gradient(ellipse 130px 110px at 230px 110px,rgba(235,238,240,.9),rgba(235,238,240,0)),
  radial-gradient(ellipse 80px 80px at 90px 230px,rgba(40,44,48,.7),rgba(40,44,48,0)),
  linear-gradient(160deg,#e4e6e7 0%,#aeb3b6 40%,#7b8185 70%,#55595c 100%)}
.photo-wax{background:
  radial-gradient(circle 55px at 150px 150px,#d8c25a 0%,#b9a543 55%,rgba(60,60,60,.9) 62%,rgba(60,60,60,0) 100%),
  radial-gradient(ellipse 90px 70px at 250px 60px,rgba(210,190,170,.8),rgba(210,190,170,0)),
  linear-gradient(150deg,#d2d4d6 0%,#9fa3a7 45%,#6d7175 100%)}
.photo-degrease{background:
  radial-gradient(circle 95px at 215px 160px,#b7a79a 0%,#8c7c70 45%,#5d5550 75%,rgba(60,55,50,0) 100%),
  radial-gradient(ellipse 40px 90px at 40px 170px,rgba(30,110,200,.85),rgba(30,110,200,0)),
  radial-gradient(ellipse 60px 40px at 40px 40px,rgba(200,140,120,.8),rgba(200,140,120,0)),
  linear-gradient(135deg,#b4b2ae,#6e6a66 50%,#353230)}
.service-bar{left:0;bottom:0;width:100%;height:46px;background:rgba(31,23,105,.85);display:flex;align-items:center;justify-content:space-between;padding:0 12px 0 18px}
.service-bar h3{font-size:17px;color:var(--white)}
.btn-red{background:var(--red);color:var(--white);font-family:"Montserrat",Arial,sans-serif;font-weight:700;font-size:10px;padding:6px 12px;text-decoration:none}

/* vehicle types */
.vehicles{left:0;top:1130px;width:1200px;height:220px;background:var(--navy)}
.vehicle{top:0;height:220px}
.vehicle-divider{top:0;width:1px;height:220px;background:rgba(255,255,255,.25)}
.vehicle h3{font-size:17px;color:var(--white);position:absolute;top:40px}
.vehicle p{position:absolute;top:80px;width:170px;font-size:11px;line-height:16px;color:var(--white)}

/* welcome */
.welcome{left:0;top:1350px;width:1200px;height:500px;background:var(--grey-bg)}
.welcome-frame{left:490px;top:47px;width:590px;height:393px;background:var(--white);border:3px solid #e2e2e2;outline:6px solid var(--white)}
.welcome-photo{left:153px;top:82px;width:390px;height:316px;background:
  radial-gradient(ellipse 90px 80px at 150px 130px,rgba(120,110,190,.85),rgba(150,140,210,.4) 60%,rgba(150,140,210,0)),
  radial-gradient(ellipse 120px 40px at 280px 110px,rgba(150,110,90,.7),rgba(150,110,90,0)),
  linear-gradient(135deg,#5f93bf 0%,#a7cbe6 35%,#e2eef7 60%,#9cc3e0 100%)}
.welcome-text{left:600px;top:118px;width:410px}
.welcome-text h2{font-family:"Open Sans",Arial,sans-serif;font-weight:700;font-size:20px;color:var(--ink);margin-bottom:16px}
.welcome-text p{font-size:11px;line-height:16px;color:var(--text);margin-bottom:16px}

/* testimonials */
.testimonials{left:0;top:1850px;width:1200px;height:418px;background:
  radial-gradient(ellipse 330px 110px at 740px 200px,rgba(170,180,190,.55),rgba(120,130,140,.25) 60%,rgba(0,0,0,0)),
  linear-gradient(180deg,#39434c 0%,#262e35 40%,#1c2328 70%,#262d33 100%)}
.quote-text{left:375px;top:150px;width:450px;text-align:center;font-size:15px;line-height:21px;color:var(--white)}
.quote-mark{font-family:Georgia,serif;font-size:64px;color:#cfd3d6;line-height:1}
.client{width:1200px;text-align:center;top:318px}
.client strong{display:block;font-family:"Montserrat",Arial,sans-serif;font-size:16px;color:var(--white)}
.client span{font-size:11px;color:#d8d8d8}

/* highlights */
.highlights{left:0;top:2268px;width:1200px;height:134px;background:var(--white)}
.highlight{top:42px;width:300px;display:flex;gap:18px}
.highlight h4{font-family:"Montserrat",Arial,sans-serif;font-weight:700;font-size:14px;color:var(--ink);margin-bottom:6px}
.highlight p{font-size:11px;line-height:16px;width:210px}
.highlight-divider{top:30px;width:1px;height:78px;background:var(--rule)}

/* footer */
.site-footer{left:0;top:2402px;width:1200px;height:367px;background:var(--blue);color:var(--white)}
.footer-head{font-family:"Montserrat",Arial,sans-serif;font-weight:700;font-size:12px;color:var(--white)}
.social-row{display:flex;align-items:center;gap:14px;font-size:11px;margin-bottom:16px}
.social-dot{width:27px;height:27px;border-radius:50%;background:var(--navy)}
.contact-row{display:flex;gap:14px;font-size:11px;line-height:17px;margin-bottom:16px}
.footer-menu a{display:block;color:var(--white);text-decoration:none;font-size:11px;line-height:18px}
.footer-map{left:720px;top:50px;width:352px;height:277px;background:
  radial-gradient(ellipse 120px 90px at 90px 70px,rgba(210,222,210,.9),rgba(210,222,210,0)),
  radial-gradient(ellipse 140px 80px at 260px 210px,rgba(215,218,228,.9),rgba(215,218,228,0)),
  linear-gradient(135deg,#eef0ec,#e1e4e0 50%,#e9ebe7)}
.footer-rule{left:135px;top:263px;width:525px;height:1px;background:rgba(255,255,255,.6)}
.copyright{left:135px;top:304px;font-size:11px}
</style>
</head>
<body>

<header class="site-header abs">
  <a class="brand abs" href="#home">
    <span class="brand-dot"></span>
    <span class="brand-name">Keystone Mobile Detailing</span>
  </a>
  <div class="call-icon abs">
    <svg width="20" height="20" viewBox="0 0 24 24"><path fill="#1f1769" d="M6.6 10.8a15.1 15.1 0 0 0 6.6 6.6l2.2-2.2a1 1 0 0 1 1-.25 11.4 11.4 0 0 0 3.6.57 1 1 0 0 1 1 1V20a1 1 0 0 1-1 1A17 17 0 0 1 3 4a1 1 0 0 1 1-1h3.5a1 1 0 0 1 1 1c0 1.25.2 2.45.57 3.57a1 1 0 0 1-.25 1z"/></svg>
  </div>
  <div class="call-label abs">CALL US NOW ON</div>
  <a class="call-number abs" href="tel:5550184420">555-018-4420</a>
  <nav class="main-nav abs">
    <a class="active" href="#home">HOME</a>
    <a href="#about">ABOUT US</a>
    <a href="#services">SERVICES</a>
    <a href="#cars">CARS</a>
    <a href="#boats">BOATS</a>
    <a href="#airplanes">AIRPLANES</a>
    <a href="#contact">CONTACT US</a>
  </nav>
</header>

<section class="hero abs" role="img" aria-label="White car covered in foam inside an automatic car wash bay">
  <div class="hero-caption abs">
    <h1 class="hero-title heading">CAR WASHING<br>SERVICES</h1>
    <a class="btn-blue" href="#services">READ MORE</a>
  </div>
  <div class="hero-dots abs"><span></span><span></span><span class="on"></span><span></span><span></span></div>
</section>

<section class="services abs" id="services">
  <h2 class="section-title heading abs" style="top:40px">OUR SERVICES</h2>
  <div class="title-rule abs" style="top:82px"></div>
  <article class="service-card abs" style="left:132px">
    <div class="service-photo photo-wash" role="img" aria-label="Pressure washer rinsing a silver car"></div>
    <div class="service-bar abs"><h3 class="heading">WASH</h3><a class="btn-red" href="#wash">READ MORE</a></div>
  </article>
  <article class="service-card abs" style="left:450px">
    <div class="service-photo photo-wax" role="img" aria-label="Hand polisher waxing a car panel"></div>
    <div class="service-bar abs"><h3 class="heading">WAX</h3><a class="btn-red" href="#wax">READ MORE</a></div>
  </article>
  <article class="service-card abs" style="left:768px">
    <div class="service-photo photo-degrease" role="img" aria-label="Degreaser being sprayed onto a wheel hub"></div>
    <div class="service-bar abs"><h3 class="heading">DEGREASE</h3><a class="btn-red" href="#degrease">READ MORE</a></div>
  </article>
</section>

<section class="vehicles abs">
  <div class="vehicle abs" style="left:130px" id="cars">
    <svg class="abs" style="left:0;top:45px" width="40" height="44" viewBox="0 0 40 44"><rect x="0" y="2" width="40" height="3" fill="#fff"/><rect x="18" y="5" width="4" height="6" fill="#fff"/><g fill="#fff"><circle cx="12" cy="15" r="1.5"/><circle cx="20" cy="15" r="1.5"/><circle cx="28" cy="15" r="1.5"/><circle cx="16" cy="20" r="1.5"/><circle cx="24" cy="20" r="1.5"/></g><path fill="#fff" d="M9 30l3-6h16l3 6h2v10h-4v-3H11v3H7V30z"/><circle cx="12" cy="33" r="1.8" fill="#1f1769"/><circle cx="28" cy="33" r="1.8" fill="#1f1769"/></svg>
    <h3 class="heading" style="left:90px">CARS</h3>
    <p style="left:90px">There are many variations of passages of Lorem Ipsum available, but the majority have suffered alteration in some form, by injected humour.</p>
  </div>
  <div class="vehicle-divider abs" style="left:440px"></div>
  <div class="vehicle abs" style="left:488px" id="boats">
    <svg class="abs" style="left:0;top:42px" width="56" height="48" viewBox="0 0 56 48"><path fill="#fff" d="M18 6h20v8h6v8H12v-8h6z"/><path fill="#fff" d="M4 24h48l-6 14H10z"/><path fill="none" stroke="#fff" stroke-width="2.5" d="M2 44c6-4 10 4 17 0s10 4 17 0 11 4 18 0"/></svg>
    <h3 class="heading" style="left:88px">BOATS</h3>
    <p style="left:88px">There are many variations of passages of Lorem Ipsum available, but the majority have suffered alteration in some form, by injected humour.</p>
  </div>
  <div class="vehicle-divider abs" style="left:776px"></div>
  <div class="vehicle abs" style="left:815px" id="airplanes">
    <svg class="abs" style="left:0;top:46px" width="58" height="40" viewBox="0 0 58 40"><path fill="#fff" d="M2 20c0-2 2-3 5-3h15L32 2h6l-6 15h12l5-6h4l-3 9 3 9h-4l-5-6H32l6 15h-6L22 23H7c-3 0-5-1-5-3z"/></svg>
    <h3 class="heading" style="left:88px">AIRPLANES</h3>
    <p style="left:88px">There are many variations of passages of Lorem Ipsum available, but the majority have suffered alteration in some form, by injected humour.</p>
  </div>
</section>

<section class="welcome abs" id="about">
  <div class="welcome-frame abs"></div>
  <div class="welcome-photo abs" role="img" aria-label="Gloved hand washing a car with a soapy mitt"></div>
  <div class="welcome-text abs">
    <h2>WELCOME TO OUR SITE</h2>
    <p>There are many variations of passages of Lorem Ipsum available, but the majority have suffered alteration in some form, by injected humour.</p>
    <p>It is a long established fact that a reader will be distracted by the readable content of a page when looking at its layout. The point of using Lorem Ipsum is that it has a more-or-less normal distribution of letters, as opposed to using 'Content here, content here', making it look like readable English. Many desktop publishing packages and web page</p>
    <a class="btn-red" href="#about">READ MORE</a>
  </div>
</section>

<section class="testimonials abs" role="img" aria-label="Motor yacht cruising at dusk, darkened behind the testimonial">
  <h2 class="section-title heading abs" style="top:58px;font-size:20px">TESTIMONIALS</h2>
  <div class="title-rule abs" style="top:95px"></div>
  <span class="quote-mark abs" style="left:355px;top:135px">&ldquo;</span>
  <p class="quote-text abs">There are many variations of passages of Lorem Ipsum available, but the majority have suffered alteration in some form, by injected humour, or randomised words which don't look even slightly believable. If you are going to use a passage of Lorem Ipsum, you need to be sure there isn't anything embarrassing hidden in the middle of text.</p>
  <span class="quote-mark abs" style="left:755px;top:258px">&rdquo;</span>
  <svg class="abs" style="left:498px;top:320px" width="18" height="30" viewBox="0 0 18 30"><path d="M15 3L4 15l11 12" fill="none" stroke="#fff" stroke-width="3"/></svg>
  <svg class="abs" style="left:686px;top:320px" width="18" height="30" viewBox="0 0 18 30"><path d="M3 3l11 12L3 27" fill="none" stroke="#fff" stroke-width="3"/></svg>
  <div class="client abs"><strong>MARTIN</strong><span>Australia</span></div>
</section>

<section class="highlights abs">
  <div class="highlight abs" style="left:132px">
    <svg width="32" height="30" viewBox="0 0 32 30"><rect x="0" y="12" width="7" height="17" fill="#1f1769"/><path fill="#1f1769" d="M9 13l7-11c2-1 4 0 4 3l-1 6h9c2 0 4 2 3 4l-3 11c-1 2-2 3-4 3H9z"/></svg>
    <div><h4>Customer Satisfaction</h4><p>There are many variations of passages of Lorem Ipsum availabl</p></div>
  </div>
  <div class="highlight-divider abs" style="left:442px"></div>
  <div class="highlight abs" style="left:472px">
    <svg width="32" height="30" viewBox="0 0 32 30"><path d="M4 18v-3a12 12 0 0 1 24 0v3" fill="none" stroke="#1f1769" stroke-width="3"/><rect x="2" y="16" width="7" height="11" rx="2" fill="#1f1769"/><rect x="23" y="16" width="7" height="11" rx="2" fill="#1f1769"/></svg>
    <div><h4>Support</h4><p>There are many variations of passages of Lorem Ipsum availabl</p></div>
  </div>
  <div class="highlight-divider abs" style="left:770px"></div>
  <div class="highlight abs" style="left:806px">
    <svg width="32" height="30" viewBox="0 0 32 30"><rect x="11" y="3" width="10" height="5" fill="none" stroke="#1f1769" stroke-width="2.5"/><rect x="1" y="8" width="30" height="20" rx="2" fill="#1f1769"/><rect x="1" y="16" width="30" height="2" fill="#fff"/></svg>
    <div><h4>30 Years Experience</h4><p>There are many variations of passages of Lorem Ipsum availabl</p></div>
  </div>
</section>

<footer class="site-footer abs" id="contact">
  <div class="abs" style="left:135px;top:56px">
    <h5 class="footer-head" style="margin-bottom:14px">FOLLOW US</h5>
    <div class="social-row"><span class="social-dot"></span>Friendpage</div>
    <div class="social-row"><span class="social-dot"></span>Chirpline</div>
    <div class="social-row"><span class="social-dot"></span>Worknet</div>
  </div>
  <div class="abs" style="left:337px;top:52px">
    <h5 class="footer-head" style="margin-bottom:16px">CONTACT US</h5>
    <div class="contact-row"><svg width="10" height="14" viewBox="0 0 10 14"><path fill="#fff" d="M5 0a5 5 0 0 1 5 5c0 4-5 9-5 9S0 9 0 5a5 5 0 0 1 5-5z"/><circle cx="5" cy="5" r="2" fill="#1b96e6"/></svg><span>118 Harbor Crest Lane<br>Vero Beach, FL 32960</span></div>
    <div class="contact-row"><svg width="12" height="12" viewBox="0 0 24 24"><path fill="#fff" d="M6.6 10.8a15.1 15.1 0 0 0 6.6 6.6l2.2-2.2a1 1 0 0 1 1-.25 11.4 11.4 0 0 0 3.6.57 1 1 0 0 1 1 1V20a1 1 0 0 1-1 1A17 17 0 0 1 3 4a1 1 0 0 1 1-1h3.5a1 1 0 0 1 1 1c0 1.25.2 2.45.57 3.57a1 1 0 0 1-.25 1z"/></svg><span>555-018-4420</span></div>
    <div class="contact-row"><svg width="12" height="10" viewBox="0 0 12 10"><rect width="12" height="10" fill="#fff"/><path d="M0 0l6 5 6-5" fill="none" stroke="#1b96e6" stroke-width="1.2"/></svg><span>info@keystonemobile.com</span></div>
  </div>
  <div class="abs footer-menu" style="left:593px;top:52px">
    <h5 class="footer-head" style="margin-bottom:14px">MENU</h5>
    <a href="#home">Home</a><a href="#about">About Us</a><a href="#services">Services</a><a href="#blog">Blog</a><a href="#contact">Contact Us</a>
  </div>
  <div class="footer-map abs" role="img" aria-label="Street map showing the business location"></div>
  <div class="footer-rule abs"></div>
  <p class="copyright abs">Copyrights @ 2018 All Rights Reserved</p>
</footer>

</body>
</html>
```